Harbor Grid Pals needs a Ad design for products page

We need an Ad design on multiple formats for our website https://www.harborgridpals.example. Our products are mainly reports and guide for KTVR and Fleetry. We want to make sure people will see our products page easier with this ad banner. We would like to use kindly the same colors from our blog site. The Ad banner must be attractive, neutral colors and modern ad.

Target Market(s)

IT and Lumivane Products

Font styles to use
Other font styles liked:
• Google Font Lato

Colors
0792cd

Requirements
Must have
• We would like to use kindly the same colors from our blog site. The Ad banner must be attractive, neutral colors and modern ad.
Nice to have
• Nothing for the moment
Should not have
• Animation, no flashy

```html
<!DOCTYPE html>
<html lang="en">
<head>
<meta charset="utf-8">
<title>Harbor Grid Pals – KTVR Software Update Management Guide Ads</title>
<link href="https://fonts.googleapis.com/css2?family=Lato:wght@400;700;900&family=Questrial&display=swap" rel="stylesheet">
<style>
  :root {
    --stage: #eceef1;
    --card: #f7f8fa;
    --blue-deep: #1546c8;
    --blue-mid: #0a6fd6;
    --cyan: #0792cd;
    --cyan-light: #3fc4e8;
    --ink: #222428;
    --white: #ffffff;
  }
  html, body {
    margin: 0; padding: 0;
    width: 1200px; height: 1200px;
    overflow: hidden;
    background: var(--stage);
  }
  .canvas { position: relative; width: 1200px; height: 1200px; }
  .ad {
    position: absolute;
    overflow: hidden;
    background: linear-gradient(135deg, #ffffff 0%, var(--card) 55%, #eef0f3 100%);
    box-shadow: 0 6px 14px rgba(0,0,0,.18);
  }
  .ad svg { display: block; width: 100%; height: 100%; }
  .ad-square { left: 127px; top: 242px; width: 413px; height: 411px; }
  .ad-tower-narrow { left: 579px; top: 206px; width: 225px; height: 448px; }
  .ad-tower-tall { left: 843px; top: 96px; width: 225px; height: 562px; }
  .ad-leaderboard { left: 95px; top: 705px; width: 968px; height: 386px; }

  .brand-dot { fill: var(--cyan); }
  .brand-name { font-family: "Lato", sans-serif; font-weight: 400; fill: var(--cyan); }
  .band-deep { fill: var(--blue-deep); }
  .band-light { fill: var(--cyan-light); }
  .ring-outer { fill: none; stroke: var(--cyan-light); stroke-width: 4; }
  .ring-inner { fill: var(--white); stroke: var(--blue-deep); stroke-width: 5; }
  .claim { font-family: "Questrial", sans-serif; text-anchor: middle; fill: var(--ink); }
  .claim-accent { fill: var(--blue-mid); }
  .title { font-family: "Questrial", sans-serif; }
  .title-blue { fill: var(--blue-mid); }
  .title-ink { fill: var(--ink); }
  .ribbon { fill: var(--blue-mid); }
  .ribbon-fold { fill: var(--blue-deep); }
  .ribbon-text { font-family: "Lato", sans-serif; font-weight: 900; fill: var(--white); text-anchor: middle; }
</style>
</head>
<body>
<main class="canvas">

  <!-- Square -->
  <section class="ad ad-square" aria-label="Square ad">
    <svg viewBox="0 0 413 411">
      <circle class="brand-dot" cx="82" cy="64" r="13"/>
      <text class="brand-name" x="104" y="73" font-size="25">harborgridpals</text>
      <polygon class="band-light" points="0,222 413,140 413,152 0,234"/>
      <polygon class="band-deep" points="0,228 413,146 413,168 0,248"/>

      <circle class="ring-outer" cx="86" cy="187" r="72"/>
      <circle class="ring-inner" cx="86" cy="187" r="66"/>
      <text class="claim" x="86" y="176" font-size="17">MOVE</text>
      <text class="claim claim-accent" x="86" y="195" font-size="17">FORWARD</text>
      <text class="claim" x="86" y="214" font-size="17">TOGETHER</text>

      <circle class="ring-outer" cx="223" cy="191" r="69"/>
      <circle class="ring-inner" cx="223" cy="191" r="63"/>
      <text class="claim" x="223" y="160" font-size="14.5">GET</text>
      <text class="claim" x="223" y="178" font-size="14.5">COMPLETE</text>
      <text class="claim claim-accent" x="223" y="196" font-size="14.5">KTVR</text>
      <text class="claim" x="223" y="214" font-size="14.5">INSTALLATION</text>
      <text class="claim claim-accent" x="223" y="232" font-size="14.5">GUIDE</text>

      <circle class="ring-outer" cx="345" cy="170" r="58"/>
      <circle class="ring-inner" cx="345" cy="170" r="52"/>
      <text class="claim" x="345" y="158" font-size="13.5">THINKING</text>
      <text class="claim claim-accent" x="345" y="174" font-size="13.5">ONLY</text>
      <text class="claim" x="345" y="190" font-size="13.5">SOLUTIONS</text>

      <text class="title title-blue" x="206" y="299" font-size="26" text-anchor="middle">KTVR Software Update</text>
      <text class="title title-ink" x="206" y="327" font-size="25" text-anchor="middle">Management Guide</text>

      <polygon class="ribbon-fold" points="338,360 362,372 338,384"/>
      <polygon class="ribbon" points="65,350 340,348 338,376 70,382"/>
      <text class="ribbon-text" x="203" y="371" font-size="16">www.harborgridpals.example</text>
    </svg>
  </section>

  <!-- Narrow tower -->
  <section class="ad ad-tower-narrow" aria-label="Narrow tower ad">
    <svg viewBox="0 0 225 448">
      <circle class="brand-dot" cx="30" cy="31" r="9"/>
      <text class="brand-name" x="44" y="36" font-size="15">harborgridpals</text>
      <polygon class="band-deep" points="0,58 0,76 225,318 225,300"/>
      <polygon class="band-light" points="0,76 0,82 225,324 225,318"/>

      <circle class="ring-outer" cx="113" cy="108" r="66"/>
      <circle class="ring-inner" cx="113" cy="108" r="61"/>
      <text class="claim" x="113" y="96" font-size="17">MOVE</text>
      <text class="claim claim-accent" x="113" y="116" font-size="17">FORWARD</text>
      <text class="claim" x="113" y="136" font-size="17">TOGETHER</text>

      <circle class="ring-outer" cx="113" cy="214" r="61"/>
      <circle class="ring-inner" cx="113" cy="214" r="56"/>
      <text class="claim" x="113" y="190" font-size="12">GET</text>
      <text class="claim" x="113" y="204" font-size="12">COMPLETE</text>
      <text class="claim claim-accent" x="113" y="218" font-size="12">KTVR</text>
      <text class="claim" x="113" y="232" font-size="12">INSTALLATION</text>
      <text class="claim claim-accent" x="113" y="246" font-size="12">GUIDE</text>

      <circle class="ring-outer" cx="113" cy="312" r="52"/>
      <circle class="ring-inner" cx="113" cy="312" r="47"/>
      <text class="claim" x="113" y="299" font-size="12">THINKING</text>
      <text class="claim claim-accent" x="113" y="314" font-size="12">ONLY</text>
      <text class="claim" x="113" y="329" font-size="12">SOLUTIONS</text>

      <text class="title title-blue" x="115" y="390" font-size="15" text-anchor="middle">KTVR Software Update</text>
      <text class="title title-ink" x="115" y="405" font-size="13.5" text-anchor="middle">Management Guide</text>

      <polygon class="ribbon-fold" points="196,421 207,428 196,434"/>
      <polygon class="ribbon" points="40,420 198,419 197,434 42,436"/>
      <text class="ribbon-text" x="118" y="431" font-size="9">www.harborgridpals.example</text>
    </svg>
  </section>

  <!-- Tall tower -->
  <section class="ad ad-tower-tall" aria-label="Tall tower ad">
    <svg viewBox="0 0 225 562">
      <circle class="brand-dot" cx="30" cy="44" r="10"/>
      <text class="brand-name" x="46" y="50" font-size="16">harborgridpals</text>
      <polygon class="band-deep" points="0,112 0,134 225,372 225,350"/>
      <polygon class="band-light" points="0,134 0,140 225,378 225,372"/>

      <circle class="ring-outer" cx="113" cy="150" r="79"/>
      <circle class="ring-inner" cx="113" cy="150" r="73"/>
      <text class="claim" x="113" y="136" font-size="21">MOVE</text>
      <text class="claim claim-accent" x="113" y="160" font-size="21">FORWARD</text>
      <text class="claim" x="113" y="184" font-size="21">TOGETHER</text>

      <circle class="ring-outer" cx="113" cy="270" r="75"/>
      <circle class="ring-inner" cx="113" cy="270" r="69"/>
      <text class="claim" x="113" y="241" font-size="14.5">GET</text>
      <text class="claim" x="113" y="258" font-size="14.5">COMPLETE</text>
      <text class="claim claim-accent" x="113" y="275" font-size="14.5">KTVR</text>
      <text class="claim" x="113" y="292" font-size="14.5">INSTALLATION</text>
      <text class="claim claim-accent" x="113" y="309" font-size="14.5">GUIDE</text>

      <circle class="ring-outer" cx="113" cy="396" r="63"/>
      <circle class="ring-inner" cx="113" cy="396" r="57"/>
      <text class="claim" x="113" y="381" font-size="15">THINKING</text>
      <text class="claim claim-accent" x="113" y="398" font-size="15">ONLY</text>
      <text class="claim" x="113" y="415" font-size="15">SOLUTIONS</text>

      <text class="title title-blue" x="116" y="482" font-size="17" text-anchor="middle">KTVR Software Update</text>
      <text class="title title-ink" x="116" y="499" font-size="16" text-anchor="middle">Management Guide</text>

      <polygon class="ribbon-fold" points="202,513 215,521 202,528"/>
      <polygon class="ribbon" points="27,510 204,509 203,528 30,531"/>
      <text class="ribbon-text" x="114" y="524" font-size="10">www.harborgridpals.example</text>
    </svg>
  </section>

  <!-- Leaderboard -->
  <section class="ad ad-leaderboard" aria-label="Wide leaderboard ad">
    <svg viewBox="0 0 968 386">
      <polygon class="band-deep" points="920,0 960,0 686,386 630,386"/>
      <polygon class="band-light" points="960,0 1000,0 726,386 686,386"/>

      <circle class="brand-dot" cx="92" cy="86" r="30"/>
      <text class="brand-name" x="150" y="101" font-size="44">harborgridpals</text>

      <text class="title title-ink" x="48" y="196" font-size="40">KTVR Software Update</text>
      <text class="title title-blue" x="48" y="244" font-size="45" font-weight="700">Management Guide</text>

      <polygon class="ribbon-fold" points="488,312 528,325 488,340"/>
      <polygon class="ribbon" points="30,290 490,290 488,328 40,336"/>
      <text class="ribbon-text" x="262" y="321" font-size="26">www.harborgridpals.example</text>

      <circle class="ring-outer" cx="652" cy="208" r="116"/>
      <circle class="ring-inner" cx="652" cy="208" r="108"/>
      <text class="claim" x="652" y="186" font-size="31">MOVE</text>
      <text class="claim claim-accent" x="652" y="220" font-size="31">FORWARD</text>
      <text class="claim" x="652" y="254" font-size="31">TOGETHER</text>

      <circle class="ring-outer" cx="854" cy="152" r="97"/>
      <circle class="ring-inner" cx="854" cy="152" r="90"/>
      <text class="claim" x="854" y="109" font-size="20">GET</text>
      <text class="claim" x="854" y="131" font-size="20">COMPLETE</text>
      <text class="claim claim-accent" x="854" y="153" font-size="20">KTVR</text>
      <text class="claim" x="854" y="175" font-size="20">INSTALLATION</text>
      <text class="claim claim-accent" x="854" y="197" font-size="20">GUIDE</text>

      <circle class="ring-outer" cx="836" cy="284" r="75"/>
      <circle class="ring-inner" cx="836" cy="284" r="68"/>
      <text class="claim" x="836" y="267" font-size="18">THINKING</text>
      <text class="claim claim-accent" x="836" y="288" font-size="18">ONLY</text>
      <text class="claim" x="836" y="309" font-size="18">SOLUTIONS</text>
    </svg>
  </section>

</main>
</body>
</html>
```